Direct Response Landing Page for Paid Search Campaigns for TrailKeepers.com

TrailKeepers.com is a leading people search / public records company, providing consumers with instant, accurate access to public records. We are a direct response org focused on engaging the user and converting the user to a customer. Our product returns instant search results based on a name or phone search. We are looking for a landing page to test out, against our current "Home Page." We will drive traffic to this page via paid search terms (ie., "people search, find people"). We would like a landing page with a headline, search forms, CTA Search button, with features/beneifts about the service and company. Specific Key Messaging will be provided.

Target Market(s)

Consumers. Skew slightly female, ages 40+

Industry/Entity Type

It Company

Number of Pages Required

1 page

Font styles to use
Sans Serif

Requirements
Must have
• Use of Logo; upper left corner, consistent w/ TrailKeepers.com.
• Use of two HTML search forms (prefer a toggle between the two). Users must type in a search query in a search form for either:
• 1. First Name, Last Name, City, State
• 2. Phone # (area code w/ phone #)
• Call to Action: "Search" button
Should not have
• Should not include TrailKeepers.com's standard nav at the top.

```html
<!DOCTYPE html>
<html lang="en">
<head>
<meta charset="utf-8">
<title>TrailKeepers – People Search</title>
<link href="https://fonts.googleapis.com/css2?family=Raleway:wght@400;500;600;700&family=Open+Sans:wght@400;600&display=swap" rel="stylesheet">
<style>
:root{
  --brand-blue:#1f78c8;
  --brand-green:#2e9a3c;
  --navy:#0d3b73;
  --ink:#333;
  --muted:#666;
  --line:#cfcfcf;
  --panel:rgba(32,128,214,.85);
  --band-top:#44a9ea;
  --band-bottom:#1a7fe0;
  --white:#fff;
}
*{box-sizing:border-box;margin:0;padding:0}
html,body{width:922px;height:1200px;overflow:hidden;background:var(--white)}
body{position:relative;font-family:'Raleway',sans-serif;color:var(--ink)}
.site-header{position:absolute;left:0;top:0;width:922px;height:82px}
.brand-name{position:absolute;left:115px;top:24px;font-size:26px;font-weight:600;color:var(--navy);line-height:1}
.account-nav{position:absolute;right:111px;top:31px;font-size:12.5px;color:var(--muted)}
.account-nav span{margin:0 7px}
.hero{position:absolute;left:0;top:82px;width:922px;height:403px;
  background:linear-gradient(180deg,#7c8a96 0%,#56636f 45%,#3d4650 100%)}
.hero-title{position:absolute;top:64px;width:100%;text-align:center;color:var(--white);
  font-weight:700;text-shadow:0 1px 3px rgba(0,0,0,.4);line-height:1.2}
.hero-title .line1{display:block;font-size:28px}
.hero-title .line2{display:block;font-size:22px;margin-top:2px}
.search-tabs{position:absolute;left:217px;top:141px;display:flex;gap:5px}
.tab{height:32px;padding:0 13px;line-height:32px;font-size:12.5px;color:var(--white)}
.tab-name{background:var(--brand-blue)}
.tab-phone{background:var(--brand-green)}
.search-panel{position:absolute;left:217px;top:173px;width:493px;height:129px;background:var(--panel);border-radius:0 4px 4px 4px}
.field{position:absolute;top:22px}
.field label{display:block;font-size:11px;color:#e3eefa;margin-bottom:5px}
.field input{height:26px;border:1px solid #d9d9d9;background:var(--white);font-family:'Open Sans',sans-serif;font-size:9px;padding:0 8px;color:#888}
.btn-search{position:absolute;left:16px;top:73px;width:111px;height:34px;background:var(--navy);
  border:2px solid var(--white);border-radius:3px;color:var(--white);font-family:'Raleway',sans-serif;font-size:12.5px}
.slider-dots{position:absolute;top:381px;left:440px;display:flex;gap:4px}
.slider-dots i{width:12px;height:12px;border-radius:50%;background:#333}
.slider-dots i:first-child{background:var(--white)}
.section-heading{position:absolute;width:100%;text-align:center;font-size:20px;font-weight:400}
.who-heading{top:526px;color:#333}
.rule{position:absolute;top:541px;height:1px;background:var(--line)}
.feature{position:absolute;top:592px;width:210px;text-align:center}
.feature svg{display:block;margin:0 auto 14px}
.feature h3{font-size:14px;font-weight:500;color:var(--navy);line-height:1.05}
.feature h3 small{display:block;font-size:12px}
.feature p{font-family:'Open Sans',sans-serif;font-size:7.6px;color:var(--muted);line-height:1.8;margin:4px auto 0;width:200px}
.feature a{display:block;font-size:10.5px;color:#222;text-decoration:none;margin-top:3px}
.help-band{position:absolute;left:0;top:779px;width:922px;height:293px;
  background:linear-gradient(180deg,var(--band-top),var(--band-bottom))}
.help-heading{top:37px;color:var(--white)}
.help-item{position:absolute;top:92px;width:210px;text-align:center;color:var(--white)}
.help-item svg{display:block;margin:0 auto 10px}
.help-item p{font-size:11.5px;line-height:1.6}
.site-footer{position:absolute;top:1102px;width:100%;text-align:center}
.footer-links{font-size:11px;color:#333;font-weight:500}
.footer-links span{margin:0 4px}
.copyright{font-family:'Open Sans',sans-serif;font-size:8.5px;color:var(--muted);margin-top:13px}
.social{display:flex;justify-content:center;gap:12px;margin-top:10px}
.social i{width:20px;height:20px;border-radius:50%;background:#8a8a8a}
</style>
</head>
<body>
<header class="site-header">
  <div class="brand-name">TrailKeepers</div>
  <nav class="account-nav">Log In<span>|</span>My Account<span>|</span>Sign Up for a Membership</nav>
</header>

<section class="hero" role="img" aria-label="Photo of a businessman touching a digital padlock over streams of binary code and a city skyline">
  <h1 class="hero-title"><span class="line1">SINCE 1999, YOUR TRUSTED ONLINE</span><span class="line2">PEOPLE SEARCH SOURCE</span></h1>
  <div class="search-tabs"><div class="tab tab-name">Search by Name</div><div class="tab tab-phone">Search by Phone</div></div>
  <form class="search-panel">
    <div class="field" style="left:17px"><label>First Name</label><input style="width:120px" placeholder="First Name"></div>
    <div class="field" style="left:141px"><label>Last Name</label><input style="width:120px" placeholder="Last Name"></div>
    <div class="field" style="left:265px"><label>City</label><input style="width:100px" placeholder="City"></div>
    <div class="field" style="left:370px"><label>State</label><input style="width:100px" placeholder="State"></div>
    <button class="btn-search" type="button">Search Now</button>
  </form>
  <div class="slider-dots"><i></i><i></i><i></i></div>
</section>

<h2 class="section-heading who-heading">WHO WE ARE</h2>
<div class="rule" style="left:116px;width:266px"></div>
<div class="rule" style="left:546px;width:266px"></div>

<div class="feature" style="left:115px">
  <svg width="38" height="40" viewBox="0 0 38 40"><rect x="2" y="6" width="34" height="32" rx="3" fill="none" stroke="#2a8ee0" stroke-width="3"/><rect x="2" y="6" width="34" height="8" fill="#2a8ee0"/><rect x="9" y="1" width="4" height="9" rx="1" fill="#2a8ee0"/><rect x="25" y="1" width="4" height="9" rx="1" fill="#2a8ee0"/><g fill="#2a8ee0"><rect x="7" y="18" width="5" height="4"/><rect x="14" y="18" width="5" height="4"/><rect x="21" y="18" width="5" height="4"/><rect x="28" y="18" width="4" height="4"/><rect x="7" y="25" width="5" height="4"/><rect x="14" y="25" width="5" height="4"/><rect x="21" y="25" width="5" height="4"/><rect x="28" y="25" width="4" height="4"/><rect x="7" y="31" width="5" height="4"/><rect x="14" y="31" width="5" height="4"/></g></svg>
  <h3>Launched online in 1999</h3>
  <p>Donec convallis pede venenatis nibh Duis quam Nam eget lacus Aliquam erat volutpat Quisque dignissim congue leo Mauris vel</p>
  <a href="#">LEARN MORE</a>
</div>
<div class="feature" style="left:357px">
  <svg width="40" height="40" viewBox="0 0 40 40"><g fill="#2a8ee0"><circle cx="20" cy="20" r="13"/><g transform="translate(20 20)"><rect x="-4" y="-20" width="8" height="10"/><rect x="-4" y="-20" width="8" height="10" transform="rotate(45)"/><rect x="-4" y="-20" width="8" height="10" transform="rotate(90)"/><rect x="-4" y="-20" width="8" height="10" transform="rotate(135)"/><rect x="-4" y="-20" width="8" height="10" transform="rotate(180)"/><rect x="-4" y="-20" width="8" height="10" transform="rotate(225)"/><rect x="-4" y="-20" width="8" height="10" transform="rotate(270)"/><rect x="-4" y="-20" width="8" height="10" transform="rotate(315)"/></g></g><circle cx="20" cy="20" r="6" fill="#fff"/></svg>
  <h3>Leading Data-as-a-Service<small>Public Records Organization</small></h3>
  <p>Donec convallis pede venenatis nibh Duis quam Nam eget lacus Aliquam erat volutpat Quisque</p>
  <a href="#">LEARN MORE</a>
</div>
<div class="feature" style="left:598px">
  <svg width="34" height="40" viewBox="0 0 34 40"><path d="M8 18V12a9 9 0 0 1 18 0v6" fill="none" stroke="#2a8ee0" stroke-width="4"/><rect x="2" y="17" width="30" height="22" rx="3" fill="#2a8ee0"/></svg>
  <h3>Privacy and Security are<small style="font-size:14px">paramount to our Organization</small></h3>
  <p>Donec convallis pede venenatis nibh Duis quam Nam eget lacus Aliquam erat volutpat Quisque</p>
  <a href="#">LEARN MORE</a>
</div>

<section class="help-band">
  <h2 class="section-heading help-heading">HOW WE HELP</h2>
  <div class="help-item" style="left:117px">
    <svg width="68" height="74" viewBox="0 0 68 74"><polygon points="34,2 65,19 65,55 34,72 3,55 3,19" fill="none" stroke="#fff" stroke-width="2"/><circle cx="34" cy="37" r="12" fill="none" stroke="#fff" stroke-width="3.5"/><path d="M34 30v8h5" fill="none" stroke="#fff" stroke-width="2.5"/></svg>
    <p>TrailKeepers has people, phone, background, property and criminal, at your fingertips.</p>
  </div>
  <div class="help-item" style="left:357px">
    <svg width="68" height="74" viewBox="0 0 68 74"><polygon points="34,2 65,19 65,55 34,72 3,55 3,19" fill="none" stroke="#fff" stroke-width="2"/><text x="34" y="48" text-anchor="middle" font-family="Raleway,sans-serif" font-weight="700" font-size="32" fill="#fff">$</text></svg>
    <p>We do the vetting for you to access local, state and nationwide records - delivering you AFFORDABLE UNLIMITED access.</p>
  </div>
  <div class="help-item" style="left:598px">
    <svg width="68" height="74" viewBox="0 0 68 74"><polygon points="34,2 65,19 65,55 34,72 3,55 3,19" fill="none" stroke="#fff" stroke-width="2"/><circle cx="34" cy="37" r="14" fill="#fff"/><path d="M27 37l5 5 9-9" fill="none" stroke="#1f86e3" stroke-width="3.5"/></svg>
    <p>We Provide Instant Access to Billions of People Search &amp; Background Records</p>
  </div>
</section>

<footer class="site-footer">
  <div class="footer-links">People Search<span>|</span>Background Check<span>|</span>Criminal Records<span>|</span>Public Records<span>|</span>Genealogy Search<span>|</span>Reverse Phone</div>
  <div class="copyright">© 2015 Company Name &nbsp;All right reserved &nbsp;Term of Use</div>
  <div class="social"><i></i><i></i><i></i><i></i></div>
</footer>
</body>
</html>
```